Coffeeshop menu for filter tip

We want to have a cannabis (coffeeshop) menu in the size 25mm wide x 60mm wide. Some examples attached.

it must have the following text:
Menu

WEED p/g
Velotrine €16
Cinderfox €14
Tide Rambler €14
Marigolden €16
Grand Pelican €14
Copper Comet €14

HASH p/g
Baltic Ember €12
Harbor Velvet€11
Plum Rova €14
Dusk Maple €10

Target Market(s)

tourist in Amsterdam

Requirements
Nice to have
• cannabis sign leaf
• No Cigarettes allowed symbol

```html
<!DOCTYPE html>
<html lang="en">
<head>
<meta charset="utf-8">
<title>Coffeeshop Menu · Amsterdam</title>
<link rel="stylesheet" href="https://fonts.googleapis.com/css2?family=Bebas+Neue&family=Kaushan+Script&family=Rye&family=Lilita+One&family=Caveat+Brush&family=Lobster&family=Bangers&family=Knewave&family=Titan+One&family=Righteous&display=swap">
<style>
  :root {
    --page: #ffffff;
    --leaf-green: #1f8b3b;
    --leaf-green-dark: #17702f;
    --heart-red: #8a1d12;
    --ink-brown: #3a1608;
    --type-white: #ffffff;
    --accent-green: #3fb54b;
    --leaf-white: #f4f4f4;
  }
  html, body {
    margin: 0;
    padding: 0;
    width: 729px;
    height: 1200px;
    overflow: hidden;
    background: var(--page);
  }
  .menu {
    position: absolute;
    left: 185px;
    top: 182px;
    width: 351px;
    height: 840px;
    background:
      radial-gradient(ellipse 60% 48% at 45% 50%, var(--heart-red) 0%, rgba(138,29,18,0.55) 45%, rgba(138,29,18,0) 85%),
      linear-gradient(180deg, var(--leaf-green) 0%, var(--leaf-green-dark) 100%);
    overflow: hidden;
  }
  .blob {
    position: absolute;
    color: var(--type-white);
    white-space: nowrap;
    line-height: 1;
    text-shadow:
      4px 0 0 var(--ink-brown), -4px 0 0 var(--ink-brown),
      0 4px 0 var(--ink-brown), 0 -4px 0 var(--ink-brown),
      4px 4px 0 var(--ink-brown), -4px -4px 0 var(--ink-brown),
      4px -4px 0 var(--ink-brown), -4px 4px 0 var(--ink-brown),
      8px 0 2px var(--ink-brown), -8px 0 2px var(--ink-brown),
      0 8px 2px var(--ink-brown), 0 -8px 2px var(--ink-brown),
      7px 7px 3px var(--ink-brown), -7px -7px 3px var(--ink-brown),
      7px -7px 3px var(--ink-brown), -7px 7px 3px var(--ink-brown);
  }
  .title {
    left: 20px; top: 26px;
    font-family: "Bebas Neue", sans-serif;
    font-size: 60px;
    letter-spacing: 1px;
  }
  .subtitle {
    left: 20px; top: 86px;
    font-family: "Bebas Neue", sans-serif;
    font-size: 36px;
  }
  .section {
    left: 20px;
    font-family: "Lilita One", sans-serif;
    font-size: 50px;
    color: var(--accent-green);
  }
  .section--weed { top: 142px; }
  .section--hash { top: 565px; }
  .unit {
    font-family: "Bebas Neue", sans-serif;
    font-size: 28px;
  }
  .unit--weed { left: 158px; top: 162px; }
  .unit--hash { left: 150px; top: 585px; }
  .leaf-mark {
    position: absolute;
    width: 96px;
    height: 80px;
    border-radius: 50%;
    background: radial-gradient(ellipse at 50% 55%, var(--leaf-white) 0%, rgba(244,244,244,0.9) 45%, rgba(244,244,244,0) 72%);
  }
  .leaf-mark--weed { left: 232px; top: 124px; }
  .leaf-mark--hash { left: 226px; top: 542px; }
  .item { left: 18px; }
  .price {
    position: absolute;
    right: 6px;
    width: 62px;
    height: 44px;
    border-radius: 22px;
    background: var(--ink-brown);
    color: var(--type-white);
    font-family: "Righteous", sans-serif;
    font-size: 28px;
    line-height: 44px;
    text-align: center;
  }
  .f-kaushan { font-family: "Kaushan Script", cursive; font-size: 40px; }
  .f-rye { font-family: "Rye", serif; font-size: 38px; }
  .f-lilita { font-family: "Lilita One", sans-serif; font-size: 38px; }
  .f-caveat { font-family: "Caveat Brush", cursive; font-size: 42px; }
  .f-lobster { font-family: "Lobster", cursive; font-size: 40px; }
  .f-bebas { font-family: "Bebas Neue", sans-serif; font-size: 44px; }
  .f-bangers { font-family: "Bangers", cursive; font-size: 44px; font-style: italic; }
  .f-knewave { font-family: "Knewave", cursive; font-size: 29px; }
  .f-titan { font-family: "Titan One", sans-serif; font-size: 34px; }
  .f-righteous { font-family: "Righteous", sans-serif; font-size: 38px; }
</style>
</head>
<body>
  <main class="menu">
    <div class="blob title">COFFEESHOP</div>
    <div class="blob subtitle">MENU • AMSTERDAM</div>

    <div class="blob section section--weed">WEED</div>
    <div class="blob unit unit--weed">p/g</div>
    <div class="leaf-mark leaf-mark--weed" role="img" aria-label="White cannabis leaf illustration"></div>

    <div class="blob item f-kaushan" style="top:203px">Velotrine</div>
    <div class="price" style="top:203px">€16</div>
    <div class="blob item f-rye" style="top:263px">Cinderfox</div>
    <div class="price" style="top:262px">€14</div>
    <div class="blob item f-lilita" style="top:319px">Tide Rambler</div>
    <div class="price" style="top:318px">€14</div>
    <div class="blob item f-caveat" style="top:372px">Marigolden</div>
    <div class="price" style="top:373px">€16</div>
    <div class="blob item f-lobster" style="top:423px">Grand Pelican</div>
    <div class="price" style="top:425px">€14</div>
    <div class="blob item f-bebas" style="top:483px">COPPER COMET</div>
    <div class="price" style="top:483px">€14</div>

    <div class="blob section section--hash">HASH</div>
    <div class="blob unit unit--hash">p/g</div>
    <div class="leaf-mark leaf-mark--hash" role="img" aria-label="White cannabis leaf illustration"></div>

    <div class="blob item f-bangers" style="top:619px">BALTIC EMBER</div>
    <div class="price" style="top:619px">€12</div>
    <div class="blob item f-knewave" style="top:677px">Harbor Velvet</div>
    <div class="price" style="top:672px">€11</div>
    <div class="blob item f-titan" style="top:725px">PLUM ROVA</div>
    <div class="price" style="top:721px">€14</div>
    <div class="blob item f-righteous" style="top:775px">DUSK MAPLE</div>
    <div class="price" style="top:773px">€10</div>
  </main>
</body>
</html>
```